Bring Modern Tempo Business Card and logo

We need a logo design and business card for a new consulting firm called Bring Modern Tempo. We specialize in Digital Transformation of enterprises of all sizes. We help enterprises understand & significantly increase their business velocity. This requires changes in culture, organization, process and technology. We also partner with advanced technology companies to deliver tangible accelerated solutions. Methods utilized include Agile, Design Thinking, Advanced Technology Platforms (microservices, digital data, virtualization, blockchain, etc.). The final design should communicate velocity, transformation, growth and innovation.

Target Market(s)

Large Corporations and Enterprises

Contact Information for Business Card

Tagline - Charting Beyond Now

Logo Text

Bring Modern Tempo or an initial or initials or a symbol/picture

Requirements
Must have
• Front side: Logo, name of business (Bring Modern Tempo), tagline (Charting Beyond Now)
• Back side: First Name, Last Name, Title, Mobile Phone, Email, LinkedIn, URL (bringmoderntempo.com)
Nice to have
• The design should communicate velocity, transformation, growth and/or innovation.

```html
<!DOCTYPE html>
<html lang="en">
<head>
<meta charset="utf-8">
<title>Bring Modern Tempo — Business Card</title>
<link rel="stylesheet" href="https://fonts.googleapis.com/css2?family=Open+Sans:wght@400;600;700&display=swap">
<style>
  :root {
    --bg: #e4e4e4;
    --card-white: #ffffff;
    --brand-orange: #f47b20;
    --ink-dark: #2b2b2b;
    --rule-grey: #d4d4d4;
    --social-blue: #1a73b8;
    --on-orange: #ffffff;
    --on-orange-rule: rgba(255,255,255,0.7);
  }
  * { box-sizing: border-box; margin: 0; padding: 0; }
  html, body {
    width: 1200px; height: 900px; overflow: hidden;
    background: var(--bg);
    font-family: "Open Sans", Arial, sans-serif;
  }
  .sheet {
    width: 1200px; height: 900px;
    display: flex; flex-direction: column; align-items: center; justify-content: center;
    gap: 40px;
  }
  .card {
    width: 640px; height: 366px;
    border-radius: 28px;
    display: flex; flex-direction: column; align-items: center; justify-content: center;
    text-align: center;
  }
  /* Front */
  .card--front { background: var(--card-white); }
  .brand-name {
    font-size: 38px; font-weight: 700; color: var(--ink-dark);
    letter-spacing: 0.2px; line-height: 1.1;
  }
  .tagline-row {
    display: flex; align-items: center; gap: 12px; margin-top: 8px;
  }
  .tagline-row .rule { width: 54px; height: 1px; background: var(--brand-orange); }
  .tagline {
    font-size: 13px; font-weight: 600; letter-spacing: 4px; text-transform: uppercase;
    color: var(--brand-orange);
  }
  .social-row {
    display: flex; flex-direction: column; align-items: center; margin-top: 26px;
  }
  .social-row .rule { width: 260px; height: 1px; background: var(--rule-grey); }
  .social-dot {
    width: 24px; height: 24px; border-radius: 50%;
    background: var(--social-blue); margin: 10px 0;
  }
  /* Back */
  .card--back { background: var(--brand-orange); color: var(--on-orange); }
  .card--back .brand-name { color: var(--on-orange); font-size: 40px; font-weight: 600; }
  .card--back .tagline-row .rule { background: var(--on-orange-rule); width: 70px; }
  .card--back .tagline { color: var(--on-orange); font-weight: 400; letter-spacing: 5px; }
  .person { margin-top: 26px; }
  .person-name { font-size: 20px; font-weight: 700; letter-spacing: 0.5px; text-transform: uppercase; }
  .person-title { font-size: 17px; font-weight: 400; }
  .divider { width: 240px; height: 1px; background: var(--on-orange-rule); margin: 14px 0; }
  .contact { font-size: 17px; line-height: 1.4; }
  .contact b { font-weight: 700; }
</style>
</head>
<body>
  <main class="sheet">
    <section class="card card--front" aria-label="Card front">
      <div class="brand-name">Bring Modern Tempo</div>
      <div class="tagline-row">
        <span class="rule"></span>
        <span class="tagline">Charting Beyond Now</span>
        <span class="rule"></span>
      </div>
      <div class="social-row">
        <span class="rule"></span>
        <span class="social-dot" role="img" aria-label="Professional profile link"></span>
        <span class="rule"></span>
      </div>
    </section>

    <section class="card card--back" aria-label="Card back">
      <div class="brand-name">Bring Modern Tempo</div>
      <div class="tagline-row">
        <span class="rule"></span>
        <span class="tagline">Charting Beyond Now</span>
        <span class="rule"></span>
      </div>
      <div class="person">
        <div class="person-name">Marcus Ellery</div>
        <div class="person-title">Managing Director</div>
      </div>
      <div class="divider"></div>
      <div class="contact">
        <div><b>P:</b> 044-555 018 273 &nbsp;|&nbsp; <b>E:</b> info@bringmoderntempo.com</div>
        <div><b>W:</b> www.bringmoderntempo.com</div>
      </div>
    </section>
  </main>
</body>
</html>
```